VornaDerm/The experts in permanent hairremoval

Our Brand is VornaDerm and we are specialized on permantent hair removal for the body for men and woman. VornaDerm is working as a Franchise chain.
The brand should be positioned as lifestyle brand but with a medical background. People should trust in us. We take care about their body. This need to be communicated 100%.
Our system is inexpensive but we don't want to show that we are cheap. So we want to communicate that permanent hair removal is a real lifestyle product but affordable.
We already created a logo that you can see the style and colour we prefer.

Target Market(s)

Europe beginning (especially german spoken markets), Middle East, Africa

Industry/Entity Type

Hair Removal

Number of Pages Required

5+ page

Font styles to use
Serif
Other font styles liked:
• Trajan Pro

Requirements
Nice to have
• We are very open for new ideas

```html
<!DOCTYPE html>
<html lang="en">
<head>
<meta charset="utf-8">
<title>VornaDerm – The experts in permanent hair removal</title>
<link href="https://fonts.googleapis.com/css2?family=Alegreya+Sans:ital,wght@0,300;0,400;0,500;1,400&family=Lato:wght@400;700&display=swap" rel="stylesheet">
<style>
:root{
  --topbar:#2f7fa0;
  --topbar-text:#bfe3f3;
  --page:#efeff1;
  --header:#f4f4f6;
  --blue:#4fabe3;
  --blue-text:#3b93c9;
  --deep:#1f6386;
  --ink:#3c3c3c;
  --muted:#7a7a7a;
  --line:#d4d4d8;
  --card:#ffffff;
  --card-head:#e6e6e8;
  --teal:#3ea08e;
  --footer:#2e7392;
}
*{box-sizing:border-box;margin:0;padding:0}
html,body{width:1200px;height:2723px;overflow:hidden}
body{position:relative;background:var(--page);font-family:"Alegreya Sans",sans-serif;color:var(--ink)}
.abs{position:absolute}

.topbar{left:0;top:0;width:1200px;height:51px;background:linear-gradient(90deg,#2a7596,#3488aa);color:var(--topbar-text);font-size:14px}
.topbar .notice{position:absolute;left:52px;top:16px}
.topbar .notice b{color:#fff;font-weight:500}
.topbar .contact{position:absolute;top:15px;display:flex;align-items:center;gap:10px;color:#fff}

.header{left:0;top:51px;width:1200px;height:171px;background:var(--header)}
.brand{position:absolute;left:52px;top:50px;display:flex;align-items:center;gap:14px}
.brand .mark{width:40px;height:40px;border-radius:50%;background:var(--blue)}
.brand .name{font-size:44px;font-weight:400;color:#5a6470;line-height:1}
.brand .tag{position:absolute;left:54px;top:50px;font-size:8px;letter-spacing:.5px;color:#5a6470;white-space:nowrap}
.nav{position:absolute;left:465px;top:78px;display:flex;gap:23px;font-size:16px;color:#444}
.nav .active{color:var(--blue-text);position:relative}
.nav .active::after{content:"";position:absolute;left:0;top:72px;width:45px;height:3px;background:var(--blue)}

.hero{left:0;top:222px;width:1200px;height:428px;background:#fff;overflow:hidden}
.hero .photo{position:absolute;left:563px;top:0;width:637px;height:428px;background:radial-gradient(ellipse at 50% 45%,#e6c3a6 0%,#d9b08e 30%,#f1ebe6 70%,#ffffff 100%)}
.hero h1{position:absolute;left:140px;top:192px;font-size:38px;font-weight:300;color:var(--blue-text);letter-spacing:.5px}
.hero .sub{position:absolute;left:137px;top:238px;font-size:20px;font-style:italic;color:#666}
.hero .dots{position:absolute;left:556px;top:401px;display:flex;gap:19px}
.hero .dots span{width:9px;height:9px;border-radius:50%;background:#555}
.hero .dots span.off{background:none;border:1.5px solid #777}
.arrow{position:absolute}

.profile{top:684px;width:343px;height:169px;background:var(--blue);color:#fff}
.profile .avatar{position:absolute;left:25px;top:41px;width:88px;height:88px;border-radius:50%;background:linear-gradient(135deg,#c9a489,#8a6a55);border:3px solid #fff}
.profile .name{position:absolute;left:138px;top:62px;font-size:25px;font-weight:300;letter-spacing:.5px}
.profile .role{position:absolute;left:138px;top:92px;font-size:11px;font-style:italic;color:#1f5f8a}

.panel{top:890px;width:343px;height:428px;background:var(--card);border:1px solid var(--line)}
.panel .head{height:50px;background:var(--card-head);border-bottom:1px solid var(--line);padding:16px 33px;font-size:22px;font-weight:400;color:#555;letter-spacing:.5px}
.panel .foot{position:absolute;left:0;bottom:0;width:100%;height:76px;background:var(--card-head);border-top:1px solid var(--line)}
.panel p{font-family:"Lato",sans-serif;font-size:12.5px;line-height:18.5px;color:#444}
.btn{position:absolute;left:30px;top:17px;width:154px;height:42px;background:var(--blue);color:#fff;font-size:15px;display:flex;align-items:center;justify-content:center;letter-spacing:.5px}
.btn.outline{background:#fff;border:2px solid var(--blue);color:var(--blue-text)}
.field{position:absolute;left:32px;width:276px;background:#fff;border:1px solid #c9c9cd;font-family:"Lato",sans-serif;font-size:10px;color:#999;padding:0 14px;display:flex;align-items:center;justify-content:space-between}
.field.name{border-color:#8cc3e3;color:#333}

.rule{left:0;width:1200px;height:1px;background:#cfcfd3}
.product{top:1387px;width:343px;height:216px;background:#fff}
.product .img{position:absolute;left:98px;top:33px;width:147px;height:152px;background:linear-gradient(180deg,#8fb4cc 0%,#2a5d88 45%,#173d62 100%);border-radius:10px}

.stories{left:0;top:1672px;width:1200px;height:458px;background:var(--blue)}
.stories h2{position:absolute;left:0;top:26px;width:1200px;text-align:center;color:#fff;font-size:41px;font-weight:300;letter-spacing:.5px}
.story{top:174px;width:343px;height:216px;background:#f2f2f4}
.story .avatar{position:absolute;left:25px;top:-44px;width:88px;height:88px;border-radius:50%;background:linear-gradient(135deg,#c9a489,#8a6a55);border:3px solid #fff}
.story q{position:absolute;left:30px;top:72px;width:290px;font-family:"Lato",sans-serif;font-size:12.5px;line-height:19px;color:#444;quotes:"\201C" "\201D"}
.story .who{position:absolute;left:30px;top:152px;font-size:13px;color:var(--deep);letter-spacing:.3px}

.info{left:0;top:2130px;width:1200px;height:167px;background:#f1f1f3}
.info .col{position:absolute;top:40px}
.info .title{display:flex;align-items:center;gap:14px;font-size:26px;color:#555;letter-spacing:.5px}
.info .text{margin-top:12px;font-size:20px;color:#5cb2e3;line-height:26px}

.map{left:0;top:2297px;width:1200px;height:339px;background:radial-gradient(ellipse at 50% 50%,#2c7ea5 0%,#1d6288 55%,#164f73 100%)}
.footer{left:0;top:2636px;width:1200px;height:87px;background:var(--footer);color:#fff}
.footer .copy{position:absolute;left:51px;top:38px;font-size:14px;letter-spacing:.5px}
.footer .social{position:absolute;top:26px;width:34px;height:34px;border-radius:50%;border:2px solid #fff}
</style>
</head>
<body>

<div class="abs topbar">
  <div class="notice">One of our representatives will happily contact you within <b>24 hours</b>. For urgent needs call us at</div>
  <div class="contact" style="left:776px">
    <svg width="18" height="18" viewBox="0 0 24 24"><path fill="#7fc4ea" d="M6.6 10.8a15.2 15.2 0 006.6 6.6l2.2-2.2c.3-.3.7-.4 1-.2 1.1.4 2.3.6 3.6.6.6 0 1 .4 1 1V20c0 .6-.4 1-1 1A17 17 0 013 4c0-.6.4-1 1-1h3.5c.6 0 1 .4 1 1 0 1.3.2 2.5.6 3.6.1.3 0 .7-.2 1z"/></svg>
    <span>800-3917-4260</span>
  </div>
  <div class="contact" style="left:934px">
    <svg width="24" height="16" viewBox="0 0 24 16"><rect width="24" height="16" fill="#7fc4ea"/><path d="M0 0l12 9L24 0" fill="none" stroke="#2f7fa0" stroke-width="1.6"/></svg>
    <span>hello@vornaderm-mail.com</span>
  </div>
</div>

<header class="abs header">
  <div class="brand">
    <span class="mark"></span>
    <span class="name">VornaDerm</span>
    <span class="tag">THE EXPERTS IN PERMANENT HAIR REMOVAL</span>
  </div>
  <nav class="nav">
    <span class="active">HOME</span><span>STUDIOS</span><span>WHY CHOOSE THIS</span><span>FRANCHISE</span><span>ABOUT</span><span>CONTACT</span><span>ONLINE SHOP</span>
  </nav>
  <svg class="arrow" style="left:1126px;top:75px" width="24" height="24" viewBox="0 0 24 24"><circle cx="10" cy="10" r="7" fill="none" stroke="#3b93c9" stroke-width="3"/><path d="M15 15l6 6" stroke="#3b93c9" stroke-width="3.5" stroke-linecap="round"/></svg>
</header>

<section class="abs hero">
  <div class="photo" role="img" aria-label="Portrait photo of a young man with styled hair and smooth skin"></div>
  <svg class="arrow" style="left:52px;top:186px" width="30" height="56" viewBox="0 0 30 56"><path d="M26 3L5 28l21 25" fill="none" stroke="#3b93c9" stroke-width="5"/></svg>
  <svg class="arrow" style="left:1118px;top:186px" width="30" height="56" viewBox="0 0 30 56"><path d="M4 3l21 25L4 53" fill="none" stroke="#2a6f95" stroke-width="5"/></svg>
  <h1>FOR A SMOTHIER BODY</h1>
  <div class="sub">your best friend for your hair</div>
  <div class="dots"><span></span><span class="off"></span><span></span><span></span></div>
</section>

<div class="abs profile" style="left:51px">
  <div class="avatar" role="img" aria-label="Team member portrait"></div>
  <div class="name">MAREK OLSEN</div><div class="role">Salon owner</div>
</div>
<div class="abs profile" style="left:428px">
  <div class="avatar" role="img" aria-label="Team member portrait"></div>
  <div class="name">MAREK OLSEN</div><div class="role">role of person</div>
</div>
<div class="abs profile" style="left:805px">
  <div class="avatar" role="img" aria-label="Team member portrait"></div>
  <div class="name">MAREK OLSEN</div><div class="role">role of person</div>
</div>

<div class="abs panel" style="left:51px">
  <div class="head">WELCOME!</div>
  <p class="abs" style="left:33px;top:82px;width:280px">Our hair clinic office provides personalized hair care to everyone. Our entire team is dedicated to providing you with the highest standard of quality hair care with services that are tailored to meet the specific needs of everyone in the market.</p>
  <p class="abs" style="left:33px;top:205px;width:270px;color:var(--blue-text)">Our hair clinic office provides personalized hair care to everyone. Our entire team is dedicated to providing you with the highest standard of quality hair care with services that are tailored to meet the specific needs of everyone in the market.</p>
  <div class="foot"><div class="btn">READ MORE</div></div>
</div>

<div class="abs panel" style="left:428px">
  <div class="head">ABOUT</div>
  <div class="abs" style="left:66px;top:84px;width:112px;height:89px;background:linear-gradient(135deg,#e8c7b0,#c99a7e 60%,#f3f3f3)" role="img" aria-label="Photo of a couple after body laser hair removal"></div>
  <div class="abs" style="left:227px;top:117px;font-size:14px;line-height:18px;color:var(--teal)">First Visit<br>25% OFF</div>
  <div class="abs" style="left:34px;top:175px;font-size:15px;color:var(--teal)">Body Laser Hair Removal</div>
  <p class="abs" style="left:34px;top:213px;width:280px">Our hair clinic office provides personalized hair care to everyone. Our entire team is dedicated to providing you with the highest standard of quality hair care with services that are tailored to meet the specific needs of everyone in the market.</p>
  <div class="foot"><div class="btn outline">READ MORE</div></div>
</div>

<div class="abs panel" style="left:805px">
  <div class="head">BOOK YOUR APPOINTMENT</div>
  <div class="field name" style="top:84px;height:36px">Lena Hartmann</div>
  <div class="field" style="top:137px;height:35px">Gender<svg width="16" height="10" viewBox="0 0 16 10"><path d="M1 1l7 7 7-7" fill="none" stroke="#888" stroke-width="1.6"/></svg></div>
  <div class="field" style="top:188px;height:35px">Calendar<svg width="16" height="10" viewBox="0 0 16 10"><path d="M1 1l7 7 7-7" fill="none" stroke="#888" stroke-width="1.6"/></svg></div>
  <div class="foot"><div class="btn">BOOK IT</div></div>
</div>

<div class="abs rule" style="top:1353px"></div>

<svg class="arrow" style="left:55px;top:1468px" width="26" height="52" viewBox="0 0 26 52"><path d="M23 3L5 26l18 23" fill="none" stroke="#3b93c9" stroke-width="5"/></svg>
<div class="abs product" style="left:51px"><div class="img" role="img" aria-label="Product photo of two bottles of men's hair removal cream"></div></div>
<div class="abs product" style="left:428px"><div class="img" role="img" aria-label="Product photo of two bottles of men's hair removal cream"></div></div>
<div class="abs product" style="left:805px"><div class="img" role="img" aria-label="Product photo of two bottles of men's hair removal cream"></div></div>
<svg class="arrow" style="left:1119px;top:1468px" width="26" height="52" viewBox="0 0 26 52"><path d="M3 3l18 23L3 49" fill="none" stroke="#2a6f95" stroke-width="5"/></svg>

<div class="abs rule" style="top:1638px"></div>

<section class="abs stories">
  <h2>SUCCESS STORIES</h2>
  <div class="abs story" style="left:51px"><div class="avatar" role="img" aria-label="Client portrait"></div><q>Very good service. Many thanks, for taking around the clock care, to nurses. I was satisfied. I recommend to everybody.</q><div class="who">TOBIAS REINER</div></div>
  <div class="abs story" style="left:428px"><div class="avatar" role="img" aria-label="Client portrait"></div><q>Very good service. Many thanks, for taking around the clock care, to nurses. I was satisfied. I recommend to everybody.</q><div class="who">CLARA WEISS</div></div>
  <div class="abs story" style="left:805px"><div class="avatar" role="img" aria-label="Client portrait"></div><q>Very good service. Many thanks, for taking around the clock care, to nurses. I was satisfied. I recommend to everybody.</q><div class="who">SAMIR HADDAD</div></div>
</section>

<section class="abs info">
  <div class="col" style="left:82px">
    <div class="title" style="margin-left:70px"><svg width="22" height="32" viewBox="0 0 22 32"><path d="M11 0a11 11 0 00-11 11c0 8 11 21 11 21s11-13 11-21A11 11 0 0011 0z" fill="#4fabe3"/><circle cx="11" cy="11" r="4.5" fill="#f1f1f3"/></svg>ADDRESS</div>
    <div class="text">412 Linden Crescent, Dunmore,<br>D17 42KT</div>
  </div>
  <div class="col" style="left:465px">
    <div class="title" style="margin-left:60px"><svg width="32" height="32" viewBox="0 0 24 24"><path fill="#4fabe3" d="M6.6 10.8a15.2 15.2 0 006.6 6.6l2.2-2.2c.3-.3.7-.4 1-.2 1.1.4 2.3.6 3.6.6.6 0 1 .4 1 1V20c0 .6-.4 1-1 1A17 17 0 013 4c0-.6.4-1 1-1h3.5c.6 0 1 .4 1 1 0 1.3.2 2.5.6 3.6.1.3 0 .7-.2 1z"/></svg>CALL US</div>
    <div class="text">800-3917-4260 ; 800-3917-4260</div>
  </div>
  <div class="col" style="left:850px">
    <div class="title" style="margin-left:38px"><svg width="58" height="36" viewBox="0 0 58 36"><rect width="58" height="36" fill="#4fabe3"/><path d="M0 0l29 20L58 0M0 36l22-19M58 36L36 17" fill="none" stroke="#f1f1f3" stroke-width="2.5"/></svg>EMAIL US</div>
    <div class="text">hello@vornaderm-mail.com</div>
  </div>
</section>

<div class="abs map" role="img" aria-label="Street map showing the clinic location"></div>

<footer class="abs footer">
  <div class="copy">© COPYRIGHT 2015. VORNADERM. ALL RIGHTS RESERVED.</div>
  <span class="social" style="left:780px"></span>
  <span class="social" style="left:849px"></span>
  <span class="social" style="left:917px"></span>
  <span class="social" style="left:984px"></span>
  <svg class="arrow" style="left:1087px;top:22px" width="60" height="36" viewBox="0 0 60 36"><path d="M4 32L30 6l26 26" fill="none" stroke="#fff" stroke-width="7"/></svg>
</footer>

</body>
</html>
```